Social Media Graphics - Harbor Climb REVISED

Create 6-7 individual social media graphics (square size) to encourage folks to join our online course called:

The Lantern Ledger Plan
How to Launch a Multi-Million Business From Scratch
Sign Up Today!

IMPORTANT: Make the largest and most prominent text on the graphic be: How to Launch a Multi-Million Business From Scratch

For the color scheme of the graphics, let's try a blue color palette; make sure the graphics appeal to both men and women

Make sure each graphic contains 1 of the 3 pics attached (crop pic as needed); and make sure one of the graphics is all TEXT only.

Target Market(s)

men and women looking to start a business

Industry/Entity Type

Entrepreneurship

Colors
0054AA
0677BA
7BADD7
CADEEF
E8F1F8

Requirements
Must have
• All the text and use the 3 pics provided; one graphic can be all text; Simple, modern design that's easy to read

```html
<!DOCTYPE html>
<html lang="en">
<head>
<meta charset="UTF-8">
<title>The Lantern Ledger Plan – Sign Up</title>
<link rel="stylesheet" href="https://fonts.googleapis.com/css2?family=Saira+Condensed:wght@700;800&display=swap">
<style>
  :root {
    --blue-deep: #0054AA;
    --blue-mid: #0677BA;
    --blue-soft: #7BADD7;
    --blue-pale: #CADEEF;
    --blue-mist: #E8F1F8;
  }
  * { margin: 0; padding: 0; box-sizing: border-box; }
  html, body {
    width: 1200px;
    height: 1200px;
    overflow: hidden;
    background: var(--blue-soft);
  }
  .post {
    position: relative;
    width: 1200px;
    height: 1200px;
    background: var(--blue-soft);
    font-family: "Saira Condensed", "Arial Narrow", sans-serif;
  }
  .post__field {
    position: absolute;
    left: 37px;
    top: 37px;
    width: 1126px;
    height: 1126px;
    background: var(--blue-deep);
  }
  .hosts-photo {
    position: absolute;
    left: 222px;
    top: 67px;
    width: 756px;
    height: 560px;
    background: radial-gradient(ellipse at 50% 40%, #2f6fb6 0%, #1a5aa6 55%, rgba(0,84,170,0) 100%);
  }
  .course-ribbon {
    position: absolute;
    left: 222px;
    top: 619px;
    width: 756px;
    height: 83px;
  }
  .course-ribbon svg { position: absolute; inset: 0; }
  .course-ribbon__name {
    position: absolute;
    inset: 0;
    display: flex;
    align-items: center;
    justify-content: center;
    color: var(--blue-pale);
    font-weight: 700;
    font-size: 54px;
    letter-spacing: 2px;
    text-transform: uppercase;
    line-height: 1;
  }
  .headline {
    position: absolute;
    left: 0;
    width: 1200px;
    text-align: center;
    text-transform: uppercase;
    font-weight: 800;
    line-height: 1;
    letter-spacing: 2px;
  }
  .headline--top { top: 733px; font-size: 86px; color: var(--blue-pale); }
  .headline--accent { top: 820px; font-size: 90px; color: var(--blue-soft); }
  .headline--bottom { top: 907px; font-size: 86px; color: var(--blue-pale); }
  .side-bar {
    position: absolute;
    top: 858px;
    height: 18px;
    background: var(--blue-soft);
  }
  .side-bar--left { left: 37px; width: 63px; }
  .side-bar--right { left: 1100px; width: 63px; }
  .signup-button {
    position: absolute;
    left: 410px;
    top: 1038px;
    width: 371px;
    height: 91px;
    background: var(--blue-pale);
    color: var(--blue-deep);
    display: flex;
    align-items: center;
    justify-content: center;
    font-weight: 700;
    font-size: 44px;
    text-transform: uppercase;
    letter-spacing: 1px;
    line-height: 1;
  }
</style>
</head>
<body>
  <main class="post">
    <div class="post__field"></div>

    <div class="hosts-photo" role="img" aria-label="Photo of the two course hosts smiling, a man in a black turtleneck with arms crossed and a woman in a denim jacket"></div>

    <div class="course-ribbon">
      <svg width="756" height="83" viewBox="0 0 756 83" aria-hidden="true">
        <polygon points="0,0 756,0 740,41.5 756,83 0,83 16,41.5" fill="var(--blue-mid)"/>
      </svg>
      <div class="course-ribbon__name">The Lantern Ledger Plan</div>
    </div>

    <h1>
      <span class="headline headline--top">How to Launch a</span>
      <span class="headline headline--accent">Multi-Million Business</span>
      <span class="headline headline--bottom">From Scratch</span>
    </h1>

    <div class="side-bar side-bar--left"></div>
    <div class="side-bar side-bar--right"></div>

    <div class="signup-button">Sign Up Today!</div>
  </main>
</body>
</html>
```